lumina Web Portal

We are developing an internet portal with content created by and for lumina in Latin America.
This portal will contain different categories focused on relevant topics for lumina who are at the same time mothers, lovers, workers, pet-owners, ...

We are looking for design that are at the same time uncluttered, easy-to-use and obvious, and comfy. Pastel colours, buttons using traditional fonts, large space for pictures, highlighted social elements,...

Our target being the middle-class lumina, we want a design that feels comfortable, real, a bit trendy and traditional, not a Vestry & Holm design, something lumina can relate to and feel comfortable enough to come back and participate.

Examples of websites:
www.cookvault.example
dama.portalvix.example
www.cabellorivo.example
www.casserol.example
Updates

Hi dear designers. After viewing some first drafts, I have updated the brief so you might have a better understanding of what we are looking for.

Thanks

Reason: We've been away for a while, unavailable to provide adequate feedback to the designs already sent. So we're extending the deadline in order to give time to everyone to adapt their work according to the feedback we'll be providing today.

Target Market(s)

lumina between 25 and 50 years from Latin America. Mainly mothers: basically, we want lumina to interact with each other and with the content of the site so they create a strong community.

Advertisingly speaking, we want to have users, contents and FMCG brands to live together on this website.

Industry/Entity Type

Internet

Requirements
Must have
• Pastel colours for category tabs. Comfortable look & feel.

The design should include 3 different pages:
- Homepage
- Article page
- User profile

The page will be done in responsive design, so design should be thought to be adapted according to the browser (2 or 3 columns).

Thanks for doing it as a PSD file .

The design should also include:
- 8 category tabs
- Space for 728x90px and 300x600px advertising format.
- A relevant menu bar at the beginning of each page
Nice to have
• News feed/best content/most active comments zone: we need to bring forward content to our users so they'll be attracted to visit more pages of the website.

Small format to register (account).

Slider or any other moving objects.

Any idea that would facilitate and increase user participation
Should not have
• Actual text. please use Lorem Ipsum.

```html
<!DOCTYPE html>
<html lang="en">
<head>
<meta charset="utf-8">
<title>lumina – profile</title>
<link rel="stylesheet" href="https://fonts.googleapis.com/css2?family=Quicksand:wght@400;500;700&display=swap">
<style>
:root{
  --magenta:#c4006c;
  --magenta-dark:#9e0057;
  --pink:#e2108a;
  --wine:#7a0a42;
  --plum:#5e0733;
  --orange:#eeb05e;
  --orange-light:#f8dcb4;
  --sand:#fbeedd;
  --gray-band:#f1f0f0;
  --line:#d6d6d6;
  --text:#2b2b2b;
  --muted:#8a8a8a;
  --white:#ffffff;
  --photo-skin:linear-gradient(160deg,#d9b8a2,#8b6a58);
  --photo-gray:linear-gradient(180deg,#d8d8d8,#6f6f6f);
}
*{box-sizing:border-box;margin:0;padding:0}
html,body{width:787px;height:1200px;overflow:hidden;background:var(--white)}
body{position:relative;font-family:"Quicksand",sans-serif;color:var(--text);font-size:9px}
.abs{position:absolute}
/* header */
.site-header{left:0;top:0;width:787px;height:122px;background:linear-gradient(180deg,var(--magenta-dark),var(--magenta) 60%,#c8006f)}
.social-square{width:18px;height:18px;background:var(--magenta-dark);border:1px solid rgba(255,255,255,.5)}
.follow{left:102px;top:15px;color:var(--white);font-size:7px;font-weight:700}
.utility{right:138px;top:15px;color:var(--white);font-size:7px;font-weight:700;letter-spacing:.2px}
.search{left:658px;top:12px;width:102px;height:13px;background:var(--white);border-left:12px solid var(--orange)}
.hello{right:27px;top:38px;color:var(--white);font-size:7px;font-style:italic}
.user-btn{left:706px;width:54px;height:10px;background:var(--white);color:var(--magenta);font-size:6px;text-align:center;line-height:10px;font-weight:700}
.user-btn.logout{background:var(--pink);color:var(--white)}
.brand{left:27px;top:30px;color:var(--white);font-size:54px;font-weight:700;letter-spacing:-1px;line-height:1}
.main-nav{left:27px;top:101px;display:flex;gap:11px;color:var(--white);font-size:9px;font-weight:500}
.rule-orange{left:0;top:122px;width:787px;height:3px;background:var(--orange)}
.rule-pink{left:0;top:125px;width:787px;height:3px;background:var(--pink)}
/* profile band */
.profile-bar{left:0;top:128px;width:548px;height:30px;background:linear-gradient(90deg,var(--orange-light),var(--sand) 70%,#fff8f0)}
.bar-title{color:var(--white);font-weight:700;font-size:11px;top:140px}
.profile-band{left:0;top:158px;width:548px;height:158px;background:var(--gray-band)}
.avatar{left:27px;top:158px;width:76px;height:100px;background:var(--photo-skin)}
.profile-name{left:27px;top:268px;color:var(--magenta);font-size:10px;font-weight:700}
.profile-meta{left:27px;top:281px;font-size:5px}
.info{left:117px;top:166px;line-height:11px;font-size:7px}
.info .label{color:var(--magenta)}
.edit{color:var(--magenta);font-size:6px;font-weight:700}
.about{left:262px;top:164px;width:245px;font-size:9px;line-height:12px}
/* messages */
.side-head{left:548px;width:239px;height:30px;background:var(--orange);color:var(--white);font-weight:700;font-size:11px;padding:12px 0 0 14px}
.msg-tab{top:158px;height:20px;color:var(--white);font-size:7px;font-weight:700;text-align:center;line-height:20px}
.msg-open{left:548px;top:178px;width:212px;height:138px;background:#f7f6f6}
.sender{font-size:7px;color:var(--muted)}
.sender b{color:var(--magenta)}
.msg-body{left:580px;top:213px;width:160px;color:var(--muted);font-style:italic;font-size:6px;line-height:8.6px}
.msg-actions{left:580px;top:300px;color:var(--magenta);font-size:5.5px;font-weight:700}
.scroll{left:748px;top:182px;width:10px;height:128px;background:#ececec}
.scroll i{display:block;width:10px;height:30px;background:var(--orange)}
.msg-row{left:548px;width:212px;height:21px;color:var(--white);font-size:6.5px;display:flex;align-items:center;padding:0 8px 0 8px;gap:8px}
.msg-row .who b{font-weight:700}
.msg-row .when{margin-left:auto;font-weight:700}
/* section headings */
.section-title{color:var(--magenta);font-weight:700;font-size:11.5px}
.view-all{font-size:9px}
.hr{height:1px;background:var(--line)}
/* favorites */
.fav{top:356px;width:88px}
.fav-label{height:27px;color:var(--white);font-weight:700;font-size:11.5px;text-align:center;line-height:29px}
.fav-img{height:61px;background:var(--photo-gray)}
/* articles */
.article{left:27px;width:467px;height:90px}
.article .thumb{position:absolute;left:0;top:0;width:76px;height:83px}
.article .crumb{position:absolute;left:90px;top:7px;color:var(--magenta);font-weight:700;font-size:8px}
.article h3{position:absolute;left:90px;top:25px;font-weight:400;font-size:13px}
.article p{position:absolute;left:90px;top:40px;width:250px;font-size:8px;line-height:11.5px}
.article .more{position:absolute;right:0;top:76px;color:var(--magenta);font-size:5.5px}
.article .sep{position:absolute;left:0;top:86px;width:467px;height:1px;background:var(--line)}
/* connections */
.person{top:432px;width:46px}
.person .ph{height:55px}
.person .nm{color:var(--magenta);font-size:7.5px;font-weight:700;line-height:9.5px;margin-top:4px}
.slider{left:556px;top:516px;width:196px;height:8px;background:#c8c8c8}
/* chat */
.chat-row{left:548px;width:212px;background:#f6f5f5}
.chat-row .ph{position:absolute;left:0;top:0;width:50px;height:53px}
.chat-row .nm{position:absolute;left:4px;top:56px;color:var(--magenta);font-size:7.5px;font-weight:700;line-height:9.5px}
.chat-row .txt{position:absolute;left:57px;top:10px;width:140px;font-style:italic;font-size:8.5px;line-height:12.4px;background:var(--white);padding:0 0 0 5px}
.send-bar{left:548px;top:930px;width:212px;height:14px;background:var(--pink)}
.send-btn{left:717px;top:932px;width:30px;height:11px;background:var(--wine);color:var(--white);font-size:5.5px;text-align:center;line-height:11px;font-weight:700}
/* footer */
.footer-edge{left:0;width:787px;height:10px;background:#f2d3e3}
.site-footer{left:0;top:985px;width:787px;height:180px;background:var(--magenta)}
.foot-brand{left:27px;top:1021px;color:var(--white);font-size:31px;font-weight:700;letter-spacing:-.5px}
.foot-head{color:var(--orange);font-size:7px;font-weight:500;top:1031px}
.foot-list{left:173px;top:1052px;color:var(--white);font-size:6.5px;line-height:11.2px}
.foot-text{color:var(--white);font-size:6.5px;line-height:11.5px}
.email-input{left:293px;top:1093px;width:163px;height:12px;background:var(--white);color:#b9b9b9;font-style:italic;font-size:6px;padding:2px 4px}
.go{left:458px;top:1093px;width:27px;height:12px;background:var(--orange);color:var(--white);font-size:6px;font-weight:700;text-align:center;line-height:12px}
.count{background:var(--white);color:var(--magenta);font-size:4px;padding:0 2px;border-radius:2px;line-height:6px}
.phone{left:533px;top:1090px;color:var(--orange);font-size:19px;font-weight:400;display:flex;align-items:center;gap:4px}
.foot-links{right:27px;top:1147px;color:var(--white);font-size:5.5px;font-weight:700}
</style>
</head>
<body>

<header class="site-header abs">
  <div class="abs social-square" style="left:27px;top:11px"></div>
  <div class="abs social-square" style="left:49px;top:11px"></div>
  <div class="abs social-square" style="left:71px;top:11px"></div>
  <div class="abs follow">FOLLOW US</div>
  <div class="abs utility">LANGUAGES &nbsp;|&nbsp; SUPPORT &nbsp;|&nbsp; HELP</div>
  <div class="abs search"></div>
  <div class="abs hello">Hello <span style="color:var(--orange)">LORENA S.</span></div>
  <div class="abs user-btn" style="top:50px">PROFILE</div>
  <div class="abs user-btn" style="top:63px">MESSAGES (3)</div>
  <div class="abs user-btn logout" style="top:75px">LOGOUT</div>
  <div class="abs brand">lumina</div>
  <nav class="abs main-nav"><span>FAMILY</span><span>CAREER</span><span>LIFESTYLE</span><span>HEALTH &amp; BEAUTY</span><span>FASHION</span><span>BLOGS</span><span>TRAVEL</span><span>AGENDA</span></nav>
</header>
<div class="abs rule-orange"></div>
<div class="abs rule-pink"></div>

<!-- profile -->
<div class="abs profile-bar"></div>
<div class="abs bar-title" style="left:117px">INFO</div>
<div class="abs bar-title" style="left:262px">ABOUT</div>
<div class="abs profile-band"></div>
<div class="abs avatar" role="img" aria-label="Profile photo of the member"></div>
<div class="abs profile-name">Lorena S.</div>
<div class="abs profile-meta">34, teacher</div>
<div class="abs info">
  <div class="label">Location</div>
  <div>Xxxxxxxxx</div>
  <div style="height:11px"></div>
  <div><span class="label">Join in</span> 22 September 2011</div>
  <div><span class="label">Feeds</span> 123</div>
  <div><span class="label">Last login</span> in 5 May 2013</div>
  <div style="height:8px"></div>
  <div class="edit">EDIT ›</div>
</div>
<div class="abs about">Lorem dolor sit amet, mundi accusam adolescens ipsum et nostrum definitiones. Ponderum periculis moderatius at per. Te eos mundi accusam adolescens et. Lorem dolor sit amet, mundi accusam adolescens ipsum et nostrum definitiones. Ponderum periculis moderatius at per. Te eos mundi accusam adolescens et.</div>
<div class="abs edit" style="left:262px;top:242px">EDIT ›</div>

<!-- messages -->
<div class="abs side-head" style="top:128px">MESSAGES</div>
<div class="abs msg-tab" style="left:548px;width:80px;background:var(--wine)">INBOX 233 (3)</div>
<div class="abs msg-tab" style="left:628px;width:70px;background:var(--pink)">FOLDERS</div>
<div class="abs msg-tab" style="left:698px;width:62px;background:var(--pink)">NEW ✎</div>
<div class="abs msg-open"></div>
<svg class="abs" style="left:558px;top:193px" width="12" height="10" viewBox="0 0 12 10"><path d="M1 4 L6 1 L11 4 V9 H1 Z M1 4 L6 7 L11 4" fill="none" stroke="var(--magenta)" stroke-width="1"/></svg>
<div class="abs sender" style="left:580px;top:195px">Sent by <b>Clara Ruiz</b> &nbsp;&nbsp; Date <b>10 May 2013</b></div>
<div class="abs msg-body">Te eos mundi accusam adolescens, mei ex reque elitr, eu inani option mei. Te eos mundi accusam adolescens, mei ex reque elitr, eu inani option mei. Te eos mundi accusam adolescens, mei ex reque elitr, eu inani option mei. Te eos mundi accusam adolescens, mei ex reque elitr, eu inani option mei. Te eos mundi accusam adolescens, mei ex reque elitr, eu inani option mei. Te eos mundi accusam adolescens, mei ex reque elitr, eu inani option mei.</div>
<div class="abs msg-actions">FORWARD &nbsp;|&nbsp; MOVE &nbsp;|&nbsp; MARK UNREAD</div>
<div class="abs scroll"><i></i></div>
<div class="abs msg-row" style="top:316px;background:var(--pink)"><svg width="11" height="8"><rect x=".5" y=".5" width="10" height="7" fill="none" stroke="#fff"/><path d="M.5 .5 L5.5 4.5 L10.5 .5" fill="none" stroke="#fff"/></svg><span class="who">Sent by <b>Clara Ruiz</b></span><span class="when">Today</span></div>
<div class="abs msg-row" style="top:337px;background:var(--magenta-dark)"><svg width="11" height="8"><rect x=".5" y=".5" width="10" height="7" fill="none" stroke="#fff"/><path d="M.5 .5 L5.5 4.5 L10.5 .5" fill="none" stroke="#fff"/></svg><span class="who">Sent by <b>Clara Ruiz</b></span><span class="when">10 May 2013</span></div>
<div class="abs msg-row" style="top:358px;background:var(--plum)"><svg width="11" height="8"><rect x=".5" y=".5" width="10" height="7" fill="none" stroke="#fff"/><path d="M.5 .5 L5.5 4.5 L10.5 .5" fill="none" stroke="#fff"/></svg><span class="who">Sent by <b>Clara Ruiz</b></span><span class="when">6 May 2013</span></div>

<!-- favorites -->
<div class="abs section-title" style="left:27px;top:336px">FAVORITES</div>
<div class="abs view-all" style="left:457px;top:338px">view all ›</div>
<div class="abs hr" style="left:27px;top:351px;width:467px"></div>
<div class="abs fav" style="left:27px"><div class="fav-label" style="background:var(--plum)">HEALTH</div><div class="fav-img" role="img" aria-label="Person meditating by the sea"></div></div>
<div class="abs fav" style="left:122px"><div class="fav-label" style="background:var(--wine)">CAREER</div><div class="fav-img" role="img" aria-label="Smiling woman at work"></div></div>
<div class="abs fav" style="left:216px"><div class="fav-label" style="background:var(--magenta-dark)">FAMILY</div><div class="fav-img" role="img" aria-label="Mother holding a baby"></div></div>
<div class="abs fav" style="left:311px"><div class="fav-label" style="background:var(--pink)">COOKING</div><div class="fav-img" role="img" aria-label="Fresh vegetables"></div></div>
<div class="abs fav" style="left:406px"><div class="fav-label" style="background:var(--wine)">TRAVEL</div><div class="fav-img" role="img" aria-label="Eiffel tower seen from below"></div></div>

<!-- marked articles -->
<div class="abs section-title" style="left:27px;top:475px">MARKED ARTICLES</div>
<div class="abs view-all" style="left:457px;top:477px">view all ›</div>
<div class="abs hr" style="left:27px;top:493px;width:467px"></div>

<article class="abs article" style="top:496px"><div class="thumb" role="img" aria-label="Child playing on the beach" style="background:linear-gradient(160deg,#6fa7c9,#d8b483)"></div><div class="crumb">FAMILY › KIDS</div><h3>TE EOS MUNDI ACCUSAM</h3><p>Mundi accusam adolescens, mei ex reque elitr, eu inani option mei. Te eos mundi accusam adolescens, mei ex reque elitr, reque elitr, eu inani option mei.</p><div class="more">READ MORE ›</div><div class="sep"></div></article>
<article class="abs article" style="top:586px"><div class="thumb" role="img" aria-label="Portrait of a woman" style="background:linear-gradient(160deg,#a0534a,#5a2a2a)"></div><div class="crumb">CAREER › BEST JOB EVER</div><h3>TE EOS MUNDI ACCUSAM</h3><p>Et eos mundi accusam adolescens, mei ex reque elitr, eu inani option mei. Te eos mundi accusam adolescens, mei ex reque elitr, reque elitr, eu inani option mei.</p><div class="more">READ MORE ›</div><div class="sep"></div></article>
<article class="abs article" style="top:676px"><div class="thumb" role="img" aria-label="Seaside town and harbour" style="background:linear-gradient(180deg,#7fb6dc,#3c8fa0 55%,#b9a987)"></div><div class="crumb">TRAVEL › BEST DESTINATIONS</div><h3>TE EOS MUNDI ACCUSAM</h3><p>Te eos mundi accusam adolescens, mei ex reque elitr, eu inani option mei. Te eos mundi accusam adolescens, mei ex reque elitr, reque elitr, eu inani option mei.</p><div class="more">READ MORE ›</div><div class="sep"></div></article>
<article class="abs article" style="top:766px"><div class="thumb" role="img" aria-label="Fashion show outfits" style="background:linear-gradient(90deg,#3a3230,#b49a6e 50%,#2c2624)"></div><div class="crumb">FASHION › NEW TRENDS</div><h3>TE EOS MUNDI ACCUSAM</h3><p>Accusam adolescens, mei ex reque elitr, eu inani option mei. Te eos mundi accusam adolescens, mei ex reque elitr, reque elitr, eu inani option mei.</p><div class="more">READ MORE ›</div><div class="sep"></div></article>
<article class="abs article" style="top:856px"><div class="thumb" role="img" aria-label="Friends toasting with drinks" style="background:linear-gradient(160deg,#3d5fa3,#d8b690)"></div><div class="crumb">LIFESTYLE › FIND THE TIME FOR YOU</div><h3>TE EOS MUNDI ACCUSAM</h3><p>Undi accusam adolescens, mei ex reque elitr, eu inani option mei. Te eos mundi accusam adolescens, mei ex reque elitr, reque elitr, eu inani option mei.</p><div class="more">READ MORE ›</div><div class="sep"></div></article>

<!-- connections -->
<div class="abs side-head" style="top:400px;width:212px;height:24px;padding-top:7px">CONNECTIONS</div>
<div class="abs person" style="left:548px"><div class="ph" role="img" aria-label="Member photo" style="background:var(--photo-skin)"></div><div class="nm">Inés<br>Varela</div></div>
<div class="abs person" style="left:609px"><div class="ph" role="img" aria-label="Member photo" style="background:linear-gradient(160deg,#c9a88e,#4a6f95)"></div><div class="nm">Rosa<br>Duarte</div></div>
<div class="abs person" style="left:671px"><div class="ph" role="img" aria-label="Member photo" style="background:linear-gradient(160deg,#e8d8cc,#7a5a48)"></div><div class="nm">Nora<br>Medel</div></div>
<div class="abs person" style="left:735px;width:25px;overflow:hidden"><div class="ph" role="img" aria-label="Member photo" style="background:var(--photo-gray)"></div><div class="nm" style="width:46px">Rosa<br>Duarte</div></div>
<svg class="abs" style="left:548px;top:516px" width="212" height="8"><path d="M0 4 L6 0 V8 Z M212 4 L206 0 V8 Z" fill="var(--magenta)"/></svg>
<div class="abs slider"></div>
<div class="abs" style="left:665px;top:516px;width:28px;height:8px;background:var(--magenta)"></div>

<!-- chat -->
<div class="abs side-head" style="top:550px;width:212px;height:23px;padding-top:6px">CHAT</div>
<div class="abs chat-row" style="top:573px;height:82px"><div class="ph" role="img" aria-label="Member photo" style="background:var(--photo-skin)"></div><div class="nm">Lorena<br>S.</div><div class="txt" style="color:var(--magenta);top:10px;background:transparent">Lorem ipsum dolor sit amet, at derum periculis moderatius a nostrum definitiones his. signiferumque at derum periculis moderatius a nostrum his… :o)</div></div>
<div class="abs chat-row" style="top:655px;height:95px"><div class="ph" role="img" aria-label="Member photo" style="background:var(--photo-skin)"></div><div class="nm">Inés<br>Varela</div><div class="txt">Tempor hendrerit aliquando ea duo, vidit democritum mei te, id diam semper timeam ius. Neque illud facilis at derum periculis moderatius a nostrum definitiones his in nam…</div></div>
<div class="abs chat-row" style="top:750px;height:92px"><div class="ph" role="img" aria-label="Member photo" style="background:linear-gradient(160deg,#c9a88e,#4a6f95)"></div><div class="nm">Rosa<br>Duarte</div><div class="txt">Eros aeque corpora eum ex, iudicabit posidonium quolibris placerat vix at derum periculis moderatius a nostrum defin at derum periculis moderatius.</div></div>
<svg class="abs" style="left:748px;top:575px" width="12" height="266"><path d="M1 7 L6 1 L11 7 Z M1 259 L6 265 L11 259 Z" fill="var(--magenta)"/></svg>
<div class="abs" style="left:548px;top:842px;width:52px;height:88px;background:linear-gradient(180deg,var(--magenta-dark),var(--pink))"></div>
<div class="abs" style="left:600px;top:842px;width:148px;height:88px;background:var(--white);border:1px solid var(--line);color:var(--muted);font-size:9px;padding:8px">/</div>
<div class="abs" style="left:748px;top:842px;width:12px;height:88px;background:var(--magenta)"></div>
<div class="abs send-bar"></div>
<div class="abs send-btn">SEND</div>

<!-- footer -->
<div class="abs footer-edge" style="top:975px"></div>
<footer class="abs site-footer"></footer>
<div class="abs footer-edge" style="top:1165px;height:35px"></div>
<div class="abs foot-brand">lumina</div>
<div class="abs foot-head" style="left:173px">FOOTER MENU</div>
<div class="abs foot-list">FAMILY<br>CAREER<br>LIFESTYLE<br>HEALTH &amp; BEAUTY<br>FASHION<br>BLOGS<br>TRAVEL<br>EVENTS</div>
<div class="abs foot-head" style="left:293px">NEWSLETTER SIGNUP</div>
<div class="abs foot-text" style="left:293px;top:1052px">By subscribing to our mailing list<br>you will always be uptade with<br>the latest news from us.</div>
<div class="abs email-input">email address</div>
<div class="abs go">GO!</div>
<div class="abs" style="left:293px;top:1138px;width:16px;height:16px;background:var(--wine)"></div><div class="abs count" style="left:311px;top:1137px">6 789</div>
<div class="abs" style="left:334px;top:1138px;width:16px;height:16px;background:var(--wine)"></div><div class="abs count" style="left:352px;top:1137px">2 345</div>
<div class="abs" style="left:375px;top:1138px;width:16px;height:16px;background:#e88bbb"></div><div class="abs count" style="left:393px;top:1137px">1 345</div>
<div class="abs foot-head" style="left:533px">CONTACT US</div>
<div class="abs foot-text" style="left:533px;top:1050px">Any suggestions or questions, please contact us.<br>Use our support email (hello@lumina.example)<br>or call us to the number below</div>
<div class="abs phone"><svg width="14" height="16" viewBox="0 0 14 16"><path d="M3 1 L6 4 L4.5 6 Q6 10 9 12 L11 10.5 L13.5 13.5 L11 15.5 Q3 13 1 3 Z" fill="var(--orange)"/></svg>555 010 274</div>
<div class="abs foot-text" style="left:533px;top:1112px;font-size:5.5px">(Mon - Fry | 08.00AM to 07.00PM)</div>
<div class="abs foot-links"><u>TERMS AND CONDITIONS OF USE</u> &nbsp;|&nbsp; FAQS &nbsp;|&nbsp; SITEMAP &nbsp;|&nbsp; COPYRIGHTS © 2013</div>

</body>
</html>
```